Business Card Design

We need a business card design for a new company located in Missouri City, TX, entitled 'BrightPath Chiropractic & Holistic Center'. Our services include restoration of health and vitality, spinal exam, health assessment, dietary & fitness programs, lymphatic & therapeutic massage, detox & remineralize body wraps, far infrared sauna therapy

Industry/Entity Type

Business

Contact Information for Business Card

BrightPath Chiropractic & Holistic Center, Marlena Oskow LMT, 4512 Hwy. 9, Suite 310, Missouri City, TX 77381, 281-555-0193

```html
<!DOCTYPE html>
<html lang="en">
<head>
<meta charset="utf-8">
<title>BrightPath Chiropractic &amp; Holistic Center – Business Card</title>
<link href="https://fonts.googleapis.com/css2?family=Open+Sans:wght@400;600;700&display=swap" rel="stylesheet">
<style>
  :root{
    --page:#e9e6e1;
    --card-black:#0b0b0c;
    --card-black-hi:#1c1c1e;
    --white:#ffffff;
    --rule:#6d6d70;
    --name-blue:#3f8fc4;
    --teal:#2aa7a0;
    --band-top:#2b8fc7;
    --band-bottom:#0f5f8f;
    --service-green:#35d04a;
    --mark-blue:#2d7fb3;
  }
  *{box-sizing:border-box;margin:0;padding:0}
  html,body{width:1200px;height:892px;overflow:hidden}
  body{
    background:var(--page);
    font-family:"Open Sans",Arial,sans-serif;
    display:flex;flex-direction:column;align-items:center;justify-content:center;gap:36px;
  }
  .card{width:700px;height:400px;position:relative;overflow:hidden;box-shadow:0 6px 18px rgba(0,0,0,.18)}

  /* Front */
  .card--front{background:linear-gradient(160deg,var(--card-black-hi),var(--card-black) 60%);color:var(--white)}
  .brand{position:absolute;left:44px;top:48px;display:flex;align-items:center;gap:22px}
  .brand__dot{width:64px;height:64px;border-radius:50%;background:var(--teal)}
  .brand__name{font-weight:700;font-size:30px;line-height:1.05}
  .divider{position:absolute;left:44px;top:178px;width:206px;height:1px;background:var(--rule)}
  .person{position:absolute;left:44px;top:210px}
  .person__name{color:var(--name-blue);font-weight:600;font-size:27px;line-height:1.1}
  .person__role{font-weight:600;font-size:18px;margin-top:4px}
  .contact{position:absolute;left:276px;right:36px;top:196px;list-style:none;font-weight:600;font-size:15px;line-height:1.55}
  .contact li{display:flex;align-items:flex-start;gap:11px}
  .contact__icon{width:17px;height:17px;flex:none;margin-top:3px;background:var(--white);border-radius:2px;display:flex;align-items:center;justify-content:center}
  .contact__text{white-space:nowrap}

  /* Back */
  .card--back{background:var(--white)}
  .back__edge{position:absolute;right:0;top:0;width:14px;height:100%;background:var(--teal)}
  .back__band{position:absolute;left:0;top:64px;right:14px;bottom:52px;background:linear-gradient(180deg,var(--band-top),var(--band-bottom))}
  .services{position:absolute;left:40px;top:20px;color:var(--service-green);font-weight:700}
  .services__title{color:var(--white);font-size:26px;margin-bottom:8px}
  .services__list{list-style:none;font-size:18px;line-height:1.42}
  .back-mark{position:absolute;right:44px;top:128px;display:flex;flex-direction:column;align-items:center;gap:12px}
  .back-mark__dot{width:70px;height:70px;border-radius:50%;background:var(--teal)}
  .back-mark__name{color:var(--white);font-weight:700;font-size:22px}
</style>
</head>
<body>

<section class="card card--front" aria-label="Business card front">
  <div class="brand">
    <span class="brand__dot"></span>
    <h1 class="brand__name">BrightPath<br>Chiropractic &amp; Holistic Center</h1>
  </div>
  <div class="divider"></div>
  <div class="person">
    <p class="person__name">Dana Whitfield</p>
    <p class="person__role">CEO</p>
  </div>
  <ul class="contact">
    <li><span class="contact__icon"><svg width="12" height="12" viewBox="0 0 12 12"><path d="M3 1l2 2-1 1.5a6 6 0 0 0 3.5 3.5L9 7l2 2-1.5 2A9 9 0 0 1 1 2.5z" fill="#2d7fb3"/></svg></span><span class="contact__text">281-555-0193</span></li>
    <li><span class="contact__icon"><svg width="12" height="10" viewBox="0 0 12 10"><rect x=".5" y=".5" width="11" height="9" fill="none" stroke="#2d7fb3"/><path d="M.5 .5L6 5.5 11.5 .5" fill="none" stroke="#2d7fb3"/></svg></span><span class="contact__text">dana@brightpathmail.com</span></li>
    <li><span class="contact__icon"><svg width="12" height="12" viewBox="0 0 12 12"><circle cx="6" cy="6" r="5" fill="none" stroke="#2d7fb3"/><path d="M1 6h10M6 1c-3 3-3 7 0 10M6 1c3 3 3 7 0 10" fill="none" stroke="#2d7fb3"/></svg></span><span class="contact__text">www.brightpathcenter.com</span></li>
    <li><span class="contact__icon"><svg width="10" height="13" viewBox="0 0 10 13"><path d="M5 12S1 7 1 4.5a4 4 0 0 1 8 0C9 7 5 12 5 12z" fill="#2d7fb3"/><circle cx="5" cy="4.5" r="1.4" fill="#fff"/></svg></span><span class="contact__text">Marlena Oskow LMT, 4512 Hwy. 9, Suite 310<br>Missouri City, TX 77381.</span></li>
  </ul>
</section>

<section class="card card--back" aria-label="Business card back">
  <div class="back__edge"></div>
  <div class="back__band">
    <div class="services">
      <h2 class="services__title">Our Services:</h2>
      <ul class="services__list">
        <li>Restoration of health and vitality</li>
        <li>Spinal exam</li>
        <li>Health assessment</li>
        <li>Dietary &amp; fitness programs</li>
        <li>Lymphatic &amp; therapeutic massage</li>
        <li>Detox &amp; remineralize body wraps</li>
        <li>Far infrared sauna therapy</li>
      </ul>
    </div>
    <div class="back-mark">
      <span class="back-mark__dot"></span>
      <span class="back-mark__name">BrightPath</span>
    </div>
  </div>
</section>

</body>
</html>
```